Regional construction company needs a banner for vehicle wraps

We wish to add a graphic banner to our fleet of vehicles which will identify our brand. This is not a logo but rather a graphic which will assist with our branding efforts. We are a service/ construction company installing and maintaining eaves trough on homes and commercial buildings with a fleet of white trucks and cars. The work trucks are equipped with 16 ft long by 8 ft high cube boxes with our logo printed on the sides. We also have several pick up trucks and sales cars carrying our logo.
The idea is to create an eye catching stripe on an angle of about 60 degrees angle up and forward on the large trucks located to the forward, side of the box panels and opposite position on the pickups and cars located at the rear quarter panel angled up and to the rear such as a racing stripe.
The final design should make use of the colors used in our logo which is a rich blue C97 M70 Y25 K8 and silver/grey but with an additional eye catching color such as but not limited to a bright yellow or burnt orange plus black. We may also add some text describing our services such as "Installation, design, cleaning, repairs".
As our business is associated with rain, possibly a theme of clouds, rain, lightening could make the graphic exciting. We intend to add this as a wrap to the vehicle so use of photos could be incorporated into the design.
The final design should be eye catching but elegant communicating a solid and professional company.

Reason: We have decided to extend the deadline in order to allow last minute submissions.

Target Market(s)

General public

Industry/Entity Type

Construction

Font styles to use
Other font styles liked:
• Swiss

Requirements
Must have
• Bold easily recognizable from a moving vehicle.
Nice to have
• A theme around stormy weather/rain/lightning
Should not have
• Cartoon appearance

```html
<!DOCTYPE html>
<html lang="en">
<head>
<meta charset="utf-8">
<title>Summit Gutters – Vehicle Banner</title>
<link rel="stylesheet" href="https://fonts.googleapis.com/css2?family=Arimo:wght@700&family=Saira+Condensed:wght@800&display=swap">
<style>
  :root {
    --storm-blue: #0a1660;
    --cloud-navy: #050d33;
    --bolt-white: #ffffff;
    --burnt-orange: #ff4a1c;
    --amber: #ffab45;
    --service-ink: #0b1638;
    --brand-white: #ffffff;
  }
  html, body {
    margin: 0;
    padding: 0;
    width: 1200px;
    height: 585px;
    overflow: hidden;
    background: #ffffff;
  }
  .banner {
    position: relative;
    width: 1200px;
    height: 585px;
    overflow: hidden;
  }
  .banner__art {
    position: absolute;
    inset: 0;
    width: 1200px;
    height: 585px;
  }
  .storm-cloud {
    position: absolute;
    left: 40px;
    top: 20px;
    width: 600px;
    height: 560px;
    border-radius: 50%;
    background: radial-gradient(ellipse at 50% 40%, var(--cloud-navy) 0%, rgba(5,13,51,0.85) 45%, rgba(10,22,96,0) 72%);
  }
  .brand-name {
    position: absolute;
    left: 90px;
    top: 360px;
    width: 470px;
    text-align: center;
    color: var(--brand-white);
    font-family: "Arimo", Arial, sans-serif;
    font-weight: 700;
    line-height: 1;
  }
  .brand-name__main {
    display: block;
    font-size: 68px;
    letter-spacing: 1px;
  }
  .brand-name__sub {
    display: block;
    margin-top: 14px;
    font-size: 34px;
    letter-spacing: 28px;
    padding-left: 28px;
  }
  .services {
    position: absolute;
    right: 52px;
    top: 108px;
    margin: 0;
    padding: 0;
    list-style: none;
    text-align: right;
    font-family: "Saira Condensed", "Arial Narrow", sans-serif;
    font-weight: 800;
    font-size: 58px;
    line-height: 1;
    letter-spacing: 3px;
    color: var(--service-ink);
  }
  .services__item {
    height: 58px;
    margin-bottom: 51px;
  }
</style>
</head>
<body>
  <main class="banner">
    <svg class="banner__art" viewBox="0 0 1200 585" aria-hidden="true">
      <defs>
        <linearGradient id="orange-glow" x1="0" y1="0" x2="1" y2="1">
          <stop offset="0" stop-color="var(--burnt-orange)"/>
          <stop offset="0.55" stop-color="var(--burnt-orange)"/>
          <stop offset="1" stop-color="var(--amber)"/>
        </linearGradient>
      </defs>
      <rect class="panel-orange" width="1200" height="585" fill="url(#orange-glow)"/>
      <polygon class="lightning-bolt" fill="var(--bolt-white)"
        points="740,0 945,0 765,222 895,222 590,585 540,585 690,318 560,318"/>
      <polygon class="panel-blue" fill="var(--storm-blue)"
        points="0,0 740,0 560,318 690,318 540,585 0,585"/>
    </svg>

    <div class="storm-cloud" role="img" aria-label="Dark storm cloud with falling rain streaks"></div>

    <div class="brand-name">
      <span class="brand-name__main">SUMMIT</span>
      <span class="brand-name__sub">GUTTERS</span>
    </div>

    <ul class="services">
      <li class="services__item">DESIGN</li>
      <li class="services__item">REPAIRS</li>
      <li class="services__item">CLEANING</li>
      <li class="services__item">INSTALLATION</li>
    </ul>
  </main>
</body>
</html>
```